Aerospace Private Equity Firm Needs Website

We need a website for new private equity fund called Orlin Partners. We buy smaller companies in the aerospace and industrial industries. I have attached some information about the firm. An example of a site we like that is a similar business but focused in a different sector is www.travomedic.com. www.quarnestgrove.com is a firm that also invests in aerospace companies.

Industry/Entity Type

Equity

Number of Pages Required

1 page

Colors
0555a3
33a6d7
ec1f27

```html
<!DOCTYPE html>
<html lang="en">
<head>
<meta charset="utf-8">
<title>Orlin Partners</title>
<link href="https://fonts.googleapis.com/css2?family=Mulish:wght@400;600;700;800&display=swap" rel="stylesheet">
<style>
:root{
  --navy:#0b2f72;
  --blue:#0555a3;
  --sky:#33a6d7;
  --red:#ec1f27;
  --ink:#222;
  --muted:#777;
  --faint:#b5b5b5;
  --panel:#e9ebf0;
  --soft:#f3f3f3;
  --foot:#5a5a5a;
}
*{box-sizing:border-box;margin:0;padding:0}
html,body{width:1200px;height:2951px;overflow:hidden}
body{font-family:"Mulish",sans-serif;color:var(--ink);background:#fff;position:relative}
.topbar{position:absolute;top:0;left:0;width:1200px;height:32px;background:var(--navy)}
.social{position:absolute;left:920px;top:7px;display:flex;gap:8px}
.social span{width:17px;height:17px;border-radius:3px;background:var(--red);display:block}
.login{position:absolute;left:1066px;top:9px;color:#fff;font-size:12px;font-weight:700;letter-spacing:.5px}
.header{position:absolute;top:32px;left:0;width:1200px;height:82px;background:#fff}
.brand{position:absolute;left:100px;top:26px;color:var(--navy);font-size:27px;font-weight:700}
.nav{position:absolute;left:436px;top:36px;display:flex;gap:0;font-size:12px;font-weight:700;color:var(--navy)}
.nav a{color:inherit;text-decoration:none;margin-right:44px;letter-spacing:.3px}
.nav a.active{color:var(--red)}
.hero{position:absolute;top:114px;left:0;width:1200px;height:582px;background:linear-gradient(135deg,#3f63a6 0%,#5d7fbd 45%,#2f548f 100%)}
.hero h1{position:absolute;top:214px;width:100%;text-align:center;color:#fff;font-size:86px;font-weight:700;letter-spacing:3px;line-height:1}
.hero p{position:absolute;top:306px;width:100%;text-align:center;color:#fff;font-size:38px;font-weight:400}
.sec-title{position:absolute;width:100%;text-align:center;color:var(--navy);font-size:36px;font-weight:700}
.rule{position:absolute;left:570px;width:40px;height:2px;background:var(--red)}
.card{position:absolute;top:828px;width:236px;height:248px;border:1px solid #e5e5e5;background:#fff;text-align:center}
.card svg{margin-top:46px}
.card h3{font-size:14px;font-weight:700;color:var(--navy);margin-top:16px}
.card .mini{width:36px;height:1px;background:#ccc;margin:10px auto 12px}
.card p{font-size:12px;color:var(--faint);line-height:19px;padding:0 40px}
.card a{display:block;margin-top:20px;font-size:11px;color:var(--navy);text-decoration:none}
.about{position:absolute;top:1137px;left:0;width:1200px;height:452px;background:var(--panel)}
.about h2{position:absolute;left:167px;top:76px;font-size:35px;font-weight:700;color:var(--navy)}
.about .rule{left:169px;top:139px}
.about p{position:absolute;left:167px;top:168px;width:406px;font-size:12px;line-height:19px;color:#555}
.btn{position:absolute;left:167px;top:304px;width:144px;height:36px;background:var(--navy);color:#fff;font-size:11px;font-weight:700;padding:11px 0 0 18px;letter-spacing:.4px}
.btn svg{position:absolute;right:14px;top:11px}
.video{position:absolute;left:631px;top:69px;width:409px;height:279px;background:#fff;box-shadow:0 1px 4px rgba(0,0,0,.12)}
.video .shot{position:absolute;left:10px;top:10px;width:389px;height:240px;background:linear-gradient(160deg,#f6f6f7,#d9dbe0)}
.video .bar{position:absolute;left:10px;top:250px;width:389px;height:18px;background:#000}
.video .play{position:absolute;left:181px;top:119px}
.stats{position:absolute;top:1589px;left:0;width:1200px;height:244px;background:linear-gradient(120deg,#1f4c97,#0b3a86 60%,#123f8a)}
.stats h2{position:absolute;left:148px;top:92px;color:#fff;font-size:27px;font-weight:600;line-height:35px}
.stat{position:absolute;top:78px;width:150px;text-align:center;color:#fff}
.stat b{display:block;font-size:42px;font-weight:600;line-height:46px}
.stat span{font-size:19px;font-weight:600}
.divider{position:absolute;top:78px;width:2px;height:90px;background:rgba(255,255,255,.7)}
.team{position:absolute;top:1833px;left:0;width:1200px;height:704px;background:var(--soft)}
.lede{position:absolute;width:100%;text-align:center;font-size:12px;line-height:19px;color:#555}
.person{position:absolute;top:187px;width:270px;height:454px;background:#fff}
.person .photo{height:269px}
.person h4{margin:22px 0 0 24px;font-size:15px;font-weight:700;color:#222}
.person .role{margin:3px 0 0 24px;font-size:14px;color:#555}
.person p{margin:24px 24px 0 24px;font-size:12px;line-height:19px;color:#555}
.arrow{position:absolute;top:2310px}
.partners-row{position:absolute;top:2778px;left:0;width:1200px}
.partner{position:absolute;font-size:16px;font-weight:700;color:#333;display:flex;align-items:center;gap:8px}
.partner i{display:block;width:14px;height:14px;background:#9aa3b3}
.footer{position:absolute;top:2895px;left:0;width:1200px;height:56px;background:var(--foot);color:#eee;text-align:center;font-size:12px;padding-top:20px}
</style>
</head>
<body>
<div class="topbar">
  <div class="social"><span></span><span></span><span></span><span></span></div>
  <div class="login">LOGIN</div>
</div>
<header class="header">
  <div class="brand">Orlin Partners</div>
  <nav class="nav">
    <a class="active" href="#">HOME</a><a href="#">ABOUT</a><a href="#">TEAM</a><a href="#">INVESTMENTS</a><a href="#">PORTFOLIO COMPANIES</a><a href="#">PRESS</a><a href="#">CONTACT US</a>
  </nav>
</header>

<section class="hero" role="img" aria-label="Blue-tinted photo of a jet engine and landing gear on an airport apron">
  <h1>ORLIN PARTNERS LP</h1>
  <p>$200 million with hard cap of $250 million</p>
</section>

<h2 class="sec-title" style="top:734px">Area of Interest</h2>
<div class="rule" style="top:796px"></div>

<div class="card" style="left:193px">
  <svg width="56" height="40" viewBox="0 0 56 40" fill="none" stroke="#888" stroke-width="1.5"><circle cx="22" cy="20" r="9"/><circle cx="22" cy="20" r="3.5"/><path d="M22 6v5M22 29v5M8 20h5M31 20h5M12 10l3.5 3.5M28.5 26.5 32 30M12 30l3.5-3.5M28.5 13.5 32 10"/><circle cx="44" cy="14" r="5"/><circle cx="44" cy="14" r="1.8"/></svg>
  <h3>Industry</h3><div class="mini"></div>
  <p>Orlin will invest in undervalued aerospace and industrial companies.</p>
  <a href="#">Read More »</a>
</div>
<div class="card" style="left:490px">
  <svg width="56" height="40" viewBox="0 0 56 40" fill="none" stroke="#888" stroke-width="1.5"><circle cx="28" cy="7" r="5"/><path d="M24 12h8l-2 6h-4zM25 18l-3 14h12l-3-14M19 32h18v5H19z"/></svg>
  <h3>Strategy</h3><div class="mini"></div>
  <p>Orlin will invest in undervalued aerospace and industrial companies.</p>
  <a href="#">Read More »</a>
</div>
<div class="card" style="left:793px">
  <svg width="56" height="40" viewBox="0 0 56 40" fill="none" stroke="#888" stroke-width="1.5"><path d="M10 38V8h6v30M16 38V22l10 6v-6l10 6v-6l10 6v10z"/><path d="M16 6c4-4 10-2 12 0s8 2 10-1"/></svg>
  <h3>Industry</h3><div class="mini"></div>
  <p>Orlin will invest in undervalued aerospace and industrial companies.</p>
  <a href="#">Read More »</a>
</div>

<section class="about">
  <h2>Orlin Partners</h2>
  <div class="rule"></div>
  <p>Orlin Partners (“Orlin”) is a Los Angeles, California-based private equity firm formed in 2016 by Principals from Westmere Park Associates (WPA). Orlin focuses on lower middle-market control investments in aerospace and industrial companies based in North America. The Orlin team has invested successfully in these sectors over a 10 - year period while at WPA.</p>
  <div class="btn">READ MORE<svg width="8" height="14" viewBox="0 0 8 14"><path d="M1 1l6 6-6 6" stroke="#fff" stroke-width="2" fill="none"/></svg></div>
  <div class="video">
    <div class="shot" role="img" aria-label="Video still of a passenger jet climbing against a white sky"></div>
    <svg class="play" width="48" height="34" viewBox="0 0 48 34"><rect width="48" height="34" rx="6" fill="#1b1b1b"/><path d="M19 10l12 7-12 7z" fill="#fff"/></svg>
    <div class="bar"></div>
  </div>
</section>

<section class="stats" role="img" aria-label="Blue-tinted photo of a business desk with documents">
  <h2>We Have 61 Years<br>of Experiences</h2>
  <div class="stat" style="left:607px"><b>1500</b><span>Clients</span></div>
  <div class="divider" style="left:760px"></div>
  <div class="stat" style="left:764px"><b>1255</b><span>Projects</span></div>
  <div class="divider" style="left:918px"></div>
  <div class="stat" style="left:922px"><b>18</b><span>Awards</span></div>
</section>

<section class="team">
  <h2 class="sec-title" style="top:46px">Team</h2>
  <div class="rule" style="top:102px"></div>
  <p class="lede" style="top:116px">Orlin Partners have had P&amp;L responsibilities in LMM Companies - invest<br>with an operational mindset</p>
  <div class="person" style="left:151px">
    <div class="photo" role="img" aria-label="Portrait of the founder" style="background:linear-gradient(180deg,#dfe6ec,#b9a08e)"></div>
    <h4>Marla Quint</h4><div class="role">Founder</div>
    <p>15 Years of International experience in product marketing, sales &amp; distribution in the aerospace and industrial sectors</p>
  </div>
  <div class="person" style="left:458px">
    <div class="photo" role="img" aria-label="Portrait of a company chief executive" style="background:linear-gradient(180deg,#9b9b9b,#d8d8d8)"></div>
    <h4>Dale Harmon</h4><div class="role">CEO of Trevin Products</div>
    <p>15 Years of International experience in product marketing, sales &amp; distribution in the aerospace and industrial sectors</p>
  </div>
  <div class="person" style="left:765px">
    <div class="photo" role="img" aria-label="Portrait of an aerospace company founder" style="background:linear-gradient(180deg,#b8b0a6,#9fb4d6)"></div>
    <h4>Neil Carver</h4><div class="role">Founder of Carver Aerospace</div>
    <p>15 Years of International experience in product marketing, sales &amp; distribution in the aerospace and industrial sectors</p>
  </div>
</section>
<svg class="arrow" style="left:40px" width="16" height="28" viewBox="0 0 16 28"><path d="M13 2 3 14l10 12" stroke="var(--navy)" stroke-width="3" fill="none"/></svg>
<svg class="arrow" style="left:1146px" width="16" height="28" viewBox="0 0 16 28"><path d="M3 2l10 12L3 26" stroke="var(--navy)" stroke-width="3" fill="none"/></svg>

<h2 class="sec-title" style="top:2594px">Our Partners</h2>
<div class="rule" style="top:2654px"></div>
<p class="lede" style="top:2684px">Orlin Partners have had P&amp;L responsibilities in LMM Companies - invest<br>with an operational mindset</p>
<div class="partners-row">
  <div class="partner" style="left:106px"><i></i>Boretek</div>
  <div class="partner" style="left:300px"><i></i>Halvern</div>
  <div class="partner" style="left:496px"><i></i>Carver Aerospace</div>
  <div class="partner" style="left:706px"><i></i>Meridian Aero</div>
  <div class="partner" style="left:898px"><i></i>Coastline Aero</div>
</div>

<footer class="footer">© 2017 Orlin Partners | Privacy Policy | User Agreement</footer>
</body>
</html>
```